An Agro-Processor Needs a Packaging Design

We need packaging designs for a range of dried fruits and jams with a family look. The line-up has five variants of dried fruits and five variants of jams (the designs to include front and back of the packaging). The entire range will be marketed under the 'Petalvyn' brand name - please find the logo attached (the logo has a lock-up with the tagline). The packaging format for the dried fruits are resealable stand-up pouches and the jams are glass bottles - please find attached pictures of the packaging formats for reference.

Please find inspiration boards for the packaging design. Also find attached inspiration board for the design style required for the back of the dried fruit packaging.

For the dried fruit packaging, we need to develop a seal that conveys organic and sugar-free claims (please find attached example of a seal)

Target Market(s)

Organic and natural living enthusiasts who would pay a premium to get the best for them and their families

Industry/Entity Type

Food Production

Font styles to use
Sans Serif
Script

Colors

Designer to choose colors to be used in the design.

Requirements
Must have
• - The brand name 'petalvyn' is inspired by the abundance of nature in Africa, it also connotes organic, natural, freshness, delicateness, airiness, sophistication and premium and therefore the design should project these values
• - The design styling to be fun, modern and 'simplistic'
• - Please find below the packaging copy for both dried fruits and jams
• DRIED FRUIT FRONT PACKAGING:
• LOGO: Petalvyn - Sharing Earth's Warmth
• FIVE VARIANT NAMES: Plucky Pineapple | Dreamy Mango | Jolly Banana | Dapper Papaya | Breezy Jackfruit
• Dried
• DEVELOP A SEAL: 100% Organic | No Added Sugar (please see example attached)
• Ugandan Origin
• Net Weight: 100g
• DRIED FRUIT BACK COPY:
• Nature's best tasting fruits are also the healthiest which is why we have made it our mission to spread nature's love! Nourished by the tropical rains on the sun-drenched soils of Africa and cultivated by the caring hands of the local farmers, our organic range of dried fruits are nutrient-dense, high in fiber and rich in minerals. Enjoy them in your salads and cereals or simply relish them as a snack! They are diet-friendly if eaten in moderation and are a natural source of energy.
• VISUAL: Stack of Fruit Visual with arrows, each with the following claims (see examples attached in the inspiration boards):
• - 100% Organic
• - No Added Sugar
• - Nutrient-Dense
• - High in Fiber
• - Rich in Minerals
• INCLUDE: Nutritional Facts Table
• Ingredients: Mango - contains 100% fruit with no added sugars, preservatives, additives, colorings or flavorings.
• Reseal the pack to maintain freshness. Store in a cool and dry place.
• INCLUDE SPACE FOR: Batch Code / Expiry Date
• Barcode
• Produced by: Temari Food Industries, P. O. Box XXXXX, Kampala - Uganda.
• Find out more about us:
• Telephone: +XXX-XXX-XXXXXX
• Email: Info@TemariFoodIndustriez.com
• www.Chatterbook.net/Petalvyn
• JAM FRONT COPY:
• FIVE VARIANT NAMES: Plucky Pineapple with a Hint of Ginger | Dreamy Mango with a Kiss of Vanilla | Jolly Banana with a Twist of Chocolate | Dapper Papaya with a Pinch of Cardamon | Breezy Jackfruit with a Touch of Cinnamon
• Jam
• Ugandan Origin
• Net Weight: 400g
• JAM BACK COPY:
• Nature's best tasting fruits are also the healthiest which is why we have made it our mission to spread nature's love! Our range of jams come from fruits that have been nourished by the tropical rains on the sun-drenched soils of Africa and have been cultivated by the caring hands of the local farmers. We pride ourselves on making sure that the jams taste as delicious and look as natural as the perfectly ripened fruit! We then make it even better by pairing it with a hint of spice! Enjoy them in your breakfast or use them as a filling in baking.
• Ingredients: Mango, citric acid, sugar, pectin, vanilla
• Barcode
• Find out more about us:

```html
<!DOCTYPE html>
<html lang="en">
<head>
<meta charset="utf-8">
<title>Petalvyn Dreamy Mango – Pouch Options</title>
<link href="https://fonts.googleapis.com/css2?family=Alex+Brush&family=Roboto:wght@400;500;700&display=swap" rel="stylesheet">
<style>
  :root {
    --backdrop: #ececec;
    --mango-yellow: #f1b322;
    --mango-yellow-deep: #e29c12;
    --mango-yellow-light: #f6c545;
    --panel-white: #fbfbfb;
    --seal-green: #1f8a3b;
    --brand-brown: #5a2a1c;
    --tagline-red: #b8344a;
    --ink: #1d1d1d;
    --ink-soft: #555555;
    --fruit-green: #7fb84a;
    --fruit-red: #b5344a;
  }
  * { box-sizing: border-box; margin: 0; padding: 0; }
  html, body { width: 720px; height: 1200px; overflow: hidden; }
  body {
    background: var(--backdrop);
    font-family: "Roboto", Arial, sans-serif;
    color: var(--ink);
  }
  .option-board {
    display: grid;
    grid-template-columns: 360px 360px;
    grid-template-rows: 600px 600px;
    width: 720px;
    height: 1200px;
  }
  .option { position: relative; }
  .option-number {
    position: absolute;
    top: 32px;
    left: 0;
    width: 100%;
    text-align: center;
    font-size: 36px;
    font-weight: 400;
    color: #111;
  }
  .pouch {
    position: absolute;
    left: 40px;
    top: 110px;
    width: 280px;
    height: 390px;
    border-radius: 10px 10px 3px 3px;
    overflow: hidden;
    background: var(--mango-yellow);
  }
  .pouch-zip {
    position: absolute;
    left: 14px;
    right: 14px;
    top: 46px;
    height: 0;
    border-top: 1px solid rgba(0,0,0,0.10);
    border-bottom: 1px solid rgba(255,255,255,0.35);
  }
  .pouch-fill { position: absolute; inset: 0; }
  .mango-pattern-fill {
    background:
      radial-gradient(circle at 20% 20%, var(--mango-yellow-light) 0 10%, transparent 35%),
      radial-gradient(circle at 80% 60%, var(--mango-yellow-light) 0 10%, transparent 35%),
      linear-gradient(180deg, var(--mango-yellow-deep), var(--mango-yellow) 50%, var(--mango-yellow-deep));
  }
  .photo-fill {
    background:
      radial-gradient(circle at 25% 15%, #9ccc5a 0 18%, transparent 30%),
      radial-gradient(circle at 85% 30%, #c9485a 0 14%, transparent 28%),
      radial-gradient(circle at 10% 70%, #c23b4e 0 14%, transparent 26%),
      radial-gradient(circle at 90% 80%, #8fbf52 0 16%, transparent 30%),
      linear-gradient(160deg, var(--fruit-green), #a8733f 55%, var(--fruit-red));
  }
  .front-panel {
    position: absolute;
    left: 54px;
    top: 86px;
    width: 172px;
    height: 304px;
    background: var(--panel-white);
    border-radius: 86px 86px 0 0;
  }
  .pouch--split { background: var(--panel-white); }
  .side-band {
    position: absolute;
    top: 0;
    bottom: 0;
    width: 52px;
  }
  .side-band--left { left: 0; }
  .side-band--right { right: 0; }
  .pack-item {
    position: absolute;
    left: 0;
    width: 100%;
    text-align: center;
    white-space: nowrap;
  }
  .organic-seal {
    left: 50%;
    width: 38px;
    height: 38px;
    margin-left: -19px;
    border-radius: 50%;
    background: var(--seal-green);
    box-shadow: inset 0 0 0 2px #fff, 0 0 0 1px var(--seal-green);
  }
  .brand-name {
    font-weight: 500;
    font-size: 24px;
    letter-spacing: -0.5px;
    color: var(--brand-brown);
    line-height: 1;
  }
  .tagline {
    font-size: 7px;
    font-weight: 500;
    color: var(--tagline-red);
    line-height: 1;
  }
  .mango-art {
    left: 50%;
    width: 70px;
    height: 74px;
    margin-left: -35px;
    border-radius: 50% 46% 50% 50%;
    background: radial-gradient(circle at 40% 40%, #f7c53a, var(--mango-yellow-deep));
  }
  .variant-name {
    font-family: "Alex Brush", cursive;
    font-size: 25px;
    line-height: 1;
    color: var(--ink);
  }
  .origin { font-size: 8px; color: var(--ink); }
  .net-weight { font-size: 5px; color: var(--ink-soft); }
</style>
</head>
<body>
<main class="option-board">

  <section class="option">
    <div class="option-number">1</div>
    <div class="pouch pouch--solid">
      <div class="pouch-zip"></div>
      <div class="front-panel"></div>
      <div class="pack-item organic-seal" style="top:106px" role="img" aria-label="Organic and no added sugar seal"></div>
      <div class="pack-item brand-name" style="top:166px">petalvyn</div>
      <div class="pack-item tagline" style="top:191px">Sharing Earth's Warmth</div>
      <div class="pack-item mango-art" style="top:218px" role="img" aria-label="Mango illustration"></div>
      <div class="pack-item variant-name" style="top:318px">Dreamy Mango</div>
      <div class="pack-item origin" style="top:354px">Ugandan Origin</div>
      <div class="pack-item net-weight" style="top:380px">Net Weight : 100g</div>
    </div>
  </section>

  <section class="option">
    <div class="option-number">2</div>
    <div class="pouch pouch--pattern">
      <div class="pouch-fill mango-pattern-fill" role="img" aria-label="Repeating small mango pattern on yellow"></div>
      <div class="front-panel"></div>
      <div class="pack-item organic-seal" style="top:106px" role="img" aria-label="Organic and no added sugar seal"></div>
      <div class="pack-item brand-name" style="top:166px">petalvyn</div>
      <div class="pack-item tagline" style="top:191px">Sharing Earth's Warmth</div>
      <div class="pack-item mango-art" style="top:218px" role="img" aria-label="Mango illustration"></div>
      <div class="pack-item variant-name" style="top:318px">Dreamy Mango</div>
      <div class="pack-item origin" style="top:354px">Ugandan Origin</div>
      <div class="pack-item net-weight" style="top:380px">Net Weight : 100g</div>
    </div>
  </section>

  <section class="option">
    <div class="option-number">3</div>
    <div class="pouch pouch--split">
      <div class="side-band side-band--left mango-pattern-fill" role="img" aria-label="Mango pattern band"></div>
      <div class="side-band side-band--right mango-pattern-fill" role="img" aria-label="Mango pattern band"></div>
      <div class="pouch-zip"></div>
      <div class="pack-item organic-seal" style="top:56px" role="img" aria-label="Organic and no added sugar seal"></div>
      <div class="pack-item brand-name" style="top:138px">petalvyn</div>
      <div class="pack-item tagline" style="top:163px">Sharing Earth's Warmth</div>
      <div class="pack-item variant-name" style="top:214px">Dreamy Mango</div>
      <div class="pack-item origin" style="top:252px">Ugandan Origin</div>
      <div class="pack-item mango-art" style="top:296px" role="img" aria-label="Mango illustration"></div>
      <div class="pack-item net-weight" style="top:382px">Net Weight : 100g</div>
    </div>
  </section>

  <section class="option">
    <div class="option-number">4</div>
    <div class="pouch pouch--photo">
      <div class="pouch-fill photo-fill" role="img" aria-label="Photograph of ripe green and red mangoes"></div>
      <div class="front-panel"></div>
      <div class="pack-item organic-seal" style="top:106px" role="img" aria-label="Organic and no added sugar seal"></div>
      <div class="pack-item brand-name" style="top:166px">petalvyn</div>
      <div class="pack-item tagline" style="top:191px">Sharing Earth's Warmth</div>
      <div class="pack-item mango-art" style="top:218px" role="img" aria-label="Mango illustration"></div>
      <div class="pack-item variant-name" style="top:318px">Dreamy Mango</div>
      <div class="pack-item origin" style="top:354px">Ugandan Origin</div>
      <div class="pack-item net-weight" style="top:380px">Net Weight : 100g</div>
    </div>
  </section>

</main>
</body>
</html>
```